依頼詳細
表面は、
ロゴ
名前
会社名
本社の住所等で、(電話はいりません)

裏面には、3つの事業の情報をお願いします。
記載項目
添付いたします
希望イメージ
シンプル 複雑
単色 カラフル
暗い 明るい
日常 高級
遊び心 厳粛
未来的 伝統的
女性的 男性的
希望する色
赤系
納品ファイル
補足説明

```html
<!DOCTYPE html>
<html lang="ja">
<head>
<meta charset="utf-8">
<title>和駿学院 名刺</title>
<link href="https://fonts.googleapis.com/css2?family=Noto+Serif+JP:wght@400;600;700&family=Noto+Sans+JP:wght@400;500;700&display=swap" rel="stylesheet">
<style>
  :root {
    --backdrop: #9d9c9c;
    --paper: #ffffff;
    --maroon: #8a1a2c;
    --ink: #2b2b2b;
    --muted: #555555;
  }
  * { margin: 0; padding: 0; box-sizing: border-box; }
  html, body { width: 846px; height: 1200px; overflow: hidden; }
  body { background: var(--backdrop); position: relative; font-family: "Noto Sans JP", sans-serif; color: var(--ink); }

  .card { position: absolute; top: 412px; width: 305px; height: 364px; background: var(--paper); overflow: hidden; }
  .card--front { left: 147px; }
  .card--back { left: 494px; }

  /* front */
  .banner { position: absolute; left: 0; top: 0; width: 305px; height: 130px; }
  .brand { position: absolute; left: 0; top: 0; width: 305px; height: 118px; display: flex; flex-direction: column; align-items: center; justify-content: center; color: var(--paper); }
  .brand__dot { width: 34px; height: 34px; border-radius: 50%; background: var(--paper); opacity: .9; margin-bottom: 6px; }
  .brand__latin { font-family: "Noto Sans JP", sans-serif; font-weight: 700; font-size: 8px; letter-spacing: .12em; }
  .brand__name { font-family: "Noto Sans JP", sans-serif; font-weight: 700; font-size: 22px; letter-spacing: .08em; margin-top: 2px; }

  .person { position: absolute; top: 158px; left: 0; width: 305px; text-align: center; }
  .person__kana { font-size: 6px; letter-spacing: .3em; color: var(--muted); }
  .person__name { font-family: "Noto Serif JP", serif; font-weight: 600; font-size: 15px; letter-spacing: .35em; margin-top: 2px; }
  .person__latin { font-family: "Noto Serif JP", serif; font-size: 6.5px; color: var(--muted); margin-top: 1px; }

  .office { position: absolute; top: 220px; left: 0; width: 305px; text-align: center; }
  .office__company { font-family: "Noto Serif JP", serif; font-weight: 600; font-size: 8.5px; color: var(--maroon); letter-spacing: .05em; }
  .office__line { font-size: 5.6px; line-height: 9px; color: var(--muted); }
  .office__company + .office__line { margin-top: 3px; }

  /* back */
  .divisions { position: absolute; top: 32px; left: 16px; width: 275px; }
  .division { border-left: 1.5px solid var(--maroon); padding-left: 5px; margin-bottom: 22px; }
  .division__title { font-size: 6.4px; font-weight: 700; color: var(--maroon); line-height: 10px; display: flex; align-items: center; }
  .division__title::before { content: ""; width: 5px; height: 5px; background: var(--maroon); margin-right: 3px; flex: none; }
  .division__line { font-size: 5.6px; line-height: 9.5px; color: var(--ink); }
</style>
</head>
<body>

<section class="card card--front" aria-label="名刺 表面">
  <svg class="banner" viewBox="0 0 305 130" aria-hidden="true">
    <polygon points="0,0 305,0 305,112 152.5,130 0,112" fill="var(--maroon)"/>
  </svg>
  <div class="brand">
    <span class="brand__dot"></span>
    <span class="brand__latin">WASHUN GAKUIN</span>
    <span class="brand__name">和駿学院</span>
  </div>

  <div class="person">
    <p class="person__kana">スルガ イチロウ</p>
    <p class="person__name">駿河 一郎</p>
    <p class="person__latin">Suruga Ichiro</p>
  </div>

  <div class="office">
    <p class="office__company">株式会社 和駿学院</p>
    <p class="office__line">〒100-0000 東京都千代田区緑町1丁目2番3号</p>
    <p class="office__line">和駿ビル5F 受付 本社事務局</p>
    <p class="office__line">https://washun-gakuin.example</p>
  </div>
</section>

<section class="card card--back" aria-label="名刺 裏面">
  <div class="divisions">
    <div class="division">
      <p class="division__title">和駿学院高等部</p>
      <p class="division__title">和駿学院専門学校</p>
      <p class="division__line">〒100-0001 東京都千代田区緑町2-4-6</p>
      <p class="division__line">TEL 03-0000-1111　FAX 03-0000-1112</p>
      <p class="division__line">https://washun-gakuin.example</p>
      <p class="division__line">E-Mail info@washun-gakuin.example</p>
    </div>
    <div class="division">
      <p class="division__title">乗馬クラブ 緑ヶ丘厩舎</p>
      <p class="division__line">〒200-0002 千葉県緑ヶ丘町3-5-7</p>
      <p class="division__line">TEL 043-000-2222　FAX 043-000-2223</p>
      <p class="division__line">https://midorigaoka.example</p>
    </div>
    <div class="division">
      <p class="division__title">ホースセラピー 駿の森 牧場</p>
      <p class="division__line">〒300-0003 茨城県駿の森町8-9-10</p>
      <p class="division__line">TEL 029-000-3333　FAX 029-000-3334</p>
      <p class="division__line">https://shun-no-mori.example</p>
    </div>
  </div>
</section>

</body>
</html>
```